Quillmark Solutions - Website for a CRM IT Services Provider to Non-profits

We need a website design for our company that provides IT services to non-profits to enable them to manage their donors and philanthropy within their organization.

We would like to see a design that uses the colors in our logo and a funky take on how to uniquely present a topic as boring as IT. Examples of sites that we really like: brantwickdale.com, www.marlowpetrie.com, tinwhistlebox.com

The final design should communicate that we are a professional, yet creative company that is fun to work with.

Target Market(s)

Non-profits who tend to be young, creative types that are low-tech

Industry/Entity Type

It Company

Requirements
Must have
• Must include tabs for Home, Contact Us, About, Projects, and Blog. The site must use the logo we have attached on all of the page, in one way or another (it can be small & in the corner).

The site has to work on all mobile browsers (iphone, ipad).
Nice to have
• It would be great if I could supply some HTML for the Contact page that would allow me to capture leads and put them directly into my CRM application. It's very easy to set up.
Should not have
• The design should not use old-style fonts and should not have a lot of dark colors. Keep it similar to our logo, clean and simple. We're not looking for a busy home page.

```html
<!DOCTYPE html>
<html lang="en">
<head>
<meta charset="utf-8">
<title>Quillmark Solutions</title>
<link rel="stylesheet" href="https://fonts.googleapis.com/css2?family=PT+Sans:wght@400;700&display=swap">
<style>
  :root {
    --cream-top: #f4f2e7;
    --cream-mid: #f2ebd5;
    --cream-low: #f5f0de;
    --teal: #1d7c9f;
    --sky: #3a9fd4;
    --sky-deep: #1f6f9c;
    --ribbon: #5f5747;
    --ribbon-dark: #3f392e;
    --ink: #4f4a3e;
    --ink-soft: #5c5648;
    --heading: #3d3b36;
    --rule: #b9b19a;
    --footer: #c8c8c6;
    --white: #ffffff;
    --icon: #8a8273;
    --social-a: #3b5a9a;
    --social-b: #3aa7e0;
    --social-c: #f4a52b;
  }
  * { box-sizing: border-box; margin: 0; padding: 0; }
  html, body { width: 886px; height: 1200px; overflow: hidden; }
  body {
    position: relative;
    font-family: "PT Sans", Arial, sans-serif;
    background: var(--cream-low);
    color: var(--ink);
  }
  .abs { position: absolute; }

  /* Header */
  .site-header { left: 0; top: 0; width: 886px; height: 150px; background: var(--cream-top); }
  .brand { left: 0; top: 18px; width: 886px; text-align: center; }
  .brand-mark { display: block; width: 54px; height: 54px; margin: 0 auto; border-radius: 50%; background: var(--teal); }
  .brand-name { display: block; margin-top: 6px; font-size: 17px; font-weight: 400; color: var(--teal); }
  .main-nav {
    left: 0; top: 119px; width: 886px;
    display: flex; justify-content: center; gap: 40px;
  }
  .main-nav a {
    font-size: 16px; font-weight: 700; letter-spacing: 0.6px;
    color: var(--teal); text-decoration: none; white-space: nowrap;
  }

  /* Hero band */
  .hero { left: 0; top: 150px; width: 886px; height: 290px; background: var(--sky); }
  .hero-text {
    left: 108px; top: 13px; width: 670px;
    text-align: center; color: var(--white);
    font-size: 16px; font-weight: 700; line-height: 26px;
  }
  .thumb {
    top: 106px; width: 152px; height: 114px;
    border: 2px solid #e8f3f8;
    background: linear-gradient(135deg, #35bde4 0%, #8fd0e0 28%, #e43c9e 55%, #f6d63c 80%, #d9488a 100%);
  }
  .hero-arrow { top: 147px; width: 34px; height: 34px; }

  /* Ribbons */
  .ribbon { left: 296px; width: 330px; height: 44px; }
  .ribbon-label {
    left: 304px; width: 314px; height: 30px; line-height: 30px;
    text-align: center; color: var(--white); font-size: 20px; font-weight: 700;
  }

  /* Services */
  .services { left: 0; top: 440px; width: 886px; height: 311px; background: var(--cream-mid); }
  .feature { top: 44px; width: 200px; text-align: center; }
  .feature-title {
    display: flex; align-items: center; justify-content: center; gap: 10px;
    font-size: 20px; font-weight: 700; color: var(--ink-soft); height: 30px;
  }
  .feature-title svg { width: 24px; height: 24px; }
  .feature p { margin-top: 10px; font-size: 11px; line-height: 17px; color: var(--ink); padding: 0 4px; }
  .col-rule { top: 78px; width: 1px; height: 142px; background: var(--rule); opacity: .7; }
  .section-rule { left: 0; top: 751px; width: 886px; height: 1px; background: var(--rule); }

  /* Blog */
  .blog-title { top: 798px; width: 300px; text-align: center; font-size: 24px; font-weight: 400; color: var(--heading); }
  .blog-image {
    top: 841px; height: 167px;
    background: linear-gradient(160deg, #31b8e3 0%, #e9ecef 22%, #e2399c 45%, #f7dc3f 65%, #e0479c 82%, #5dc4e6 100%);
  }
  .blog-text { top: 1017px; width: 316px; text-align: center; font-size: 11px; line-height: 17px; color: var(--ink); }
  .blog-rule { left: 441px; top: 862px; width: 1px; height: 136px; background: var(--rule); }

  /* Footer */
  .site-footer { left: 0; top: 1114px; width: 886px; height: 86px; background: var(--footer); }
  .copyright { left: 98px; top: 32px; font-size: 12px; color: #3c3c3c; }
  .social { top: 27px; width: 24px; height: 24px; border-radius: 2px; }
</style>
</head>
<body>

<header class="abs site-header">
  <div class="abs brand">
    <span class="brand-mark"></span>
    <span class="brand-name">Quillmark Solutions</span>
  </div>
  <nav class="abs main-nav">
    <a href="#">HOME</a>
    <a href="#">ABOUT US</a>
    <a href="#">OUR SERVICES</a>
    <a href="#">PROJECTS</a>
    <a href="#">BLOG</a>
    <a href="#">CONTACT US</a>
  </nav>
</header>

<section class="abs hero">
  <p class="abs hero-text">Lorem ipsum dolor sit ipsum Lorem ipsum dolor sit ipsumLorem ipsum dolor sit ipsumLorem ipsum dolor sit ipsumLorem ipsum dolor sit ipsum Lorem ipsum dolor sit ipsumLorem ipsum dolor sit ipsumLorem ipsum dolor sit ipsum</p>

  <svg class="abs hero-arrow" style="left:61px" viewBox="0 0 34 34" aria-label="Previous">
    <circle cx="17" cy="17" r="15" fill="none" stroke="var(--sky-deep)" stroke-width="2"/>
    <path d="M20 9 L12 17 L20 25 Z" fill="var(--sky-deep)"/>
  </svg>
  <div class="abs thumb" style="left:111px" role="img" aria-label="Project preview: colourful abstract printing artwork"></div>
  <div class="abs thumb" style="left:277px" role="img" aria-label="Project preview: colourful abstract printing artwork"></div>
  <div class="abs thumb" style="left:444px" role="img" aria-label="Project preview: colourful abstract printing artwork"></div>
  <div class="abs thumb" style="left:609px" role="img" aria-label="Project preview: colourful abstract printing artwork"></div>
  <svg class="abs hero-arrow" style="left:780px" viewBox="0 0 34 34" aria-label="Next">
    <circle cx="17" cy="17" r="15" fill="none" stroke="var(--sky-deep)" stroke-width="2"/>
    <path d="M14 9 L22 17 L14 25 Z" fill="var(--sky-deep)"/>
  </svg>
</section>

<section class="abs services">
  <div class="abs feature" style="left:99px">
    <h3 class="feature-title">
      <svg viewBox="0 0 24 24" aria-hidden="true">
        <g fill="var(--icon)">
          <circle cx="12" cy="12" r="7.5"/>
          <rect x="10" y="1" width="4" height="5"/><rect x="10" y="18" width="4" height="5"/>
          <rect x="1" y="10" width="5" height="4"/><rect x="18" y="10" width="5" height="4"/>
          <rect x="10" y="1" width="4" height="5" transform="rotate(45 12 12)"/>
          <rect x="10" y="18" width="4" height="5" transform="rotate(45 12 12)"/>
          <rect x="1" y="10" width="5" height="4" transform="rotate(45 12 12)"/>
          <rect x="18" y="10" width="5" height="4" transform="rotate(45 12 12)"/>
        </g>
        <circle cx="12" cy="12" r="3" fill="var(--cream-mid)"/>
      </svg>
      About Us
    </h3>
    <p>Lorem ipsum dolor sit ipsum Lorem ipsum dolor sit ipsum Lorem ipsum dolor sit ipsum Lorem ipsum dolor sit ipsum Lorem ipsum dolor sit ipsum Lorem ipsum dolor sit ipsum Lorem ipsum dolor sit ipsum Lorem ipsum dolor sit ipsum Lorem ipsum dolor sit ipsum Lorem ipsum dolor sit.</p>
  </div>
  <div class="abs col-rule" style="left:321px"></div>
  <div class="abs feature" style="left:342px">
    <h3 class="feature-title">
      <svg viewBox="0 0 24 24" aria-hidden="true">
        <path d="M12 2a7 7 0 0 0-4 12.7V17h8v-2.3A7 7 0 0 0 12 2z" fill="var(--icon)"/>
        <rect x="8.5" y="18" width="7" height="2" fill="var(--icon)"/>
        <rect x="9.5" y="21" width="5" height="2" rx="1" fill="var(--icon)"/>
      </svg>
      Our Services
    </h3>
    <p>Lorem ipsum dolor sit ipsum Lorem ipsum dolor sit ipsum Lorem ipsum dolor sit ipsum Lorem ipsum dolor sit ipsum Lorem ipsum dolor sit ipsum Lorem ipsum dolor sit ipsum Lorem ipsum dolor sit ipsum Lorem ipsum dolor sit ipsum Lorem ipsum dolor sit ipsum Lorem ipsum dolor sit.</p>
  </div>
  <div class="abs col-rule" style="left:561px"></div>
  <div class="abs feature" style="left:579px">
    <h3 class="feature-title">
      <svg viewBox="0 0 24 24" aria-hidden="true">
        <rect x="2" y="5" width="20" height="14" fill="none" stroke="var(--icon)" stroke-width="1.6"/>
        <path d="M2 5 L12 13 L22 5" fill="none" stroke="var(--icon)" stroke-width="1.6"/>
      </svg>
      Contact Us
    </h3>
    <p>Lorem ipsum dolor sit ipsum Lorem ipsum dolor sit ipsum Lorem ipsum dolor sit ipsum Lorem ipsum dolor sit ipsum Lorem ipsum dolor sit ipsum Lorem ipsum dolor sit ipsum Lorem ipsum dolor sit ipsum Lorem ipsum dolor sit ipsum Lorem ipsum dolor sit ipsum Lorem ipsum dolor sit.</p>
  </div>
</section>

<div class="abs section-rule"></div>

<svg class="abs ribbon" style="top:408px" viewBox="0 0 330 44" aria-hidden="true">
  <path d="M8 2 H322 V32 L316 40 L310 32 H20 L14 40 L8 32 Z" fill="var(--ribbon-dark)"/>
  <rect x="8" y="2" width="314" height="30" fill="var(--ribbon)"/>
</svg>
<h2 class="abs ribbon-label" style="top:410px">Title Heading</h2>

<svg class="abs ribbon" style="top:723px" viewBox="0 0 330 44" aria-hidden="true">
  <path d="M8 2 H322 V32 L316 40 L310 32 H20 L14 40 L8 32 Z" fill="var(--ribbon-dark)"/>
  <rect x="8" y="2" width="314" height="30" fill="var(--ribbon)"/>
</svg>
<h2 class="abs ribbon-label" style="top:725px">Title Heading</h2>

<article>
  <h3 class="abs blog-title" style="left:110px">Blog Heading</h3>
  <div class="abs blog-image" style="left:120px;width:297px" role="img" aria-label="Blog image: colourful abstract printing artwork"></div>
  <p class="abs blog-text" style="left:110px">Lorem ipsum dolor sit ipsum Lorem ipsum idolor sit ipsum Lorem ipsum dolor sit ipsum Lorem ipsum dolor sit ipsum Lorem ipsum dolor sit ipsum Lorem ipsum dolor sit ipsum Lorem ipsum dolor sit ipsum Lorem ipsum dolor sit ipsum Lorem ipsum dolor sit ipsum Lorem ipsum dolor sit ipsum Lorem ipsum dolor sit.</p>
</article>
<div class="abs blog-rule"></div>
<article>
  <h3 class="abs blog-title" style="left:470px">Blog Heading</h3>
  <div class="abs blog-image" style="left:478px;width:281px" role="img" aria-label="Blog image: colourful abstract printing artwork"></div>
  <p class="abs blog-text" style="left:462px">Lorem ipsum dolor sit ipsum Lorem ipsum idolor sit ipsum Lorem ipsum dolor sit ipsum Lorem ipsum dolor sit ipsum Lorem ipsum dolor sit ipsum Lorem ipsum dolor sit ipsum Lorem ipsum dolor sit ipsum Lorem ipsum dolor sit ipsum Lorem ipsum dolor sit ipsum Lorem ipsum dolor sit ipsum Lorem ipsum dolor sit.</p>
</article>

<footer class="abs site-footer">
  <p class="abs copyright">Copyright Text Here</p>
  <span class="abs social" style="left:690px;background:var(--social-a)" role="img" aria-label="Social link"></span>
  <span class="abs social" style="left:725px;background:var(--social-b)" role="img" aria-label="Social link"></span>
  <span class="abs social" style="left:760px;background:var(--social-c)" role="img" aria-label="Feed link"></span>
</footer>

</body>
</html>
```